Design a Job Application & CV

I need a design for upcoming job applications that includes a cv. It needs to look as elegant and modern as possible as the application will be send mainly to large corporations and strategy consultancies. I have attached an application that I like for your consideration. One of the more difficult requirements is that it needs to be editable in ms office word for mac/windows.
As stated only the design is part of this project. I will fill in my content later on.
Updates
Project Deadline Extended
Reason: Dear Designers,
I am going to increase the budget as well as extending the deadline. I am hoping that you can improve upon the design that I have provided in the brief. If you have questions please let me know.
Dear Designers,
Target Market(s)
Human Resources Managers, Senior Consultants and Executives of larger firms
Industry/Entity Type
Office
Requirements
Must have
- 4 Pages including( a cover page, a coverletter page, 2 pages cv)
It should be easy to edit and should be readable by word for mac, i.e. in the *.docx format.
Here is an example of what I like:
http://www.torvenmaal.de/applicationexample.pdf
http://www.torvenmaal.de/applicationExample.docx
colors that I like are blue, grey, black, white
Nice to have
- icons to indicate sections
Should not have
- invasive cliparts

```html
<!DOCTYPE html>
<html lang="en">
<head>
<meta charset="utf-8">
<title>Job Application &amp; CV – Page Set</title>
<link rel="stylesheet" href="https://fonts.googleapis.com/css2?family=Open+Sans:wght@300;400;600&display=swap">
<style>
  :root {
    --backdrop: #5b5b5b;
    --backdrop-dark: #3e3e3e;
    --charcoal: #2f2f2f;
    --charcoal-soft: #4a4a4a;
    --accent-blue: #00a8e6;
    --heading-blue: #2a7fc4;
    --pale-blue: #a9d9f0;
    --pale-grey: #d6d6d6;
    --text-grey: #6e6e6e;
    --text-dark: #333333;
    --paper: #ffffff;
  }
  * { margin: 0; padding: 0; box-sizing: border-box; }
  html, body { width: 840px; height: 1200px; overflow: hidden; }
  body {
    font-family: "Open Sans", Arial, sans-serif;
    background: linear-gradient(90deg, var(--backdrop-dark), var(--backdrop) 30%, var(--backdrop) 70%, var(--backdrop-dark));
    position: relative;
  }
  address { font-style: normal; }
  .page { position: absolute; background: var(--paper); overflow: hidden; }
  .abs { position: absolute; }

  /* ---------- CV pages ---------- */
  .cv-page { top: 19px; width: 400px; height: 567px; }
  .cv-page--one { left: 19px; }
  .cv-page--two { left: 422px; }
  .cv-header { position: absolute; left: 0; top: 0; width: 100%; height: 102px; }
  .cv-page--one .cv-header { background: linear-gradient(90deg, #2b2b2b, #454545 60%, #555); }
  .cv-page--two .cv-header { background: var(--accent-blue); }
  .cv-header__rule { position: absolute; left: 0; top: 102px; width: 100%; height: 5px; background: var(--accent-blue); }
  .cv-page--two .cv-header__rule { height: 12px; background: var(--charcoal); }
  .cv-name { position: absolute; left: 32px; top: 34px; font-size: 40px; font-weight: 400; letter-spacing: -0.5px; line-height: 1; }
  .cv-page--one .cv-name { color: var(--paper); }
  .cv-page--two .cv-name { color: var(--charcoal); left: 34px; }
  .cv-name__last { color: var(--accent-blue); }
  .cv-page--two .cv-name__last { color: var(--paper); }
  .cv-contact { position: absolute; left: 196px; top: 10px; font-size: 9.5px; font-weight: 600; line-height: 11.5px; color: var(--paper); }
  .cv-page--two .cv-contact { left: 200px; color: var(--charcoal); }
  .cv-footer { position: absolute; left: 0; bottom: 0; width: 100%; height: 46px; background: linear-gradient(90deg, #222, #3a3a3a 60%, #444); }

  .cv-section { position: absolute; left: 12px; width: 370px; display: grid; grid-template-columns: 138px 1fr; column-gap: 8px; row-gap: 0; }
  .cv-section__title { grid-column: 1; text-align: right; font-size: 12px; font-weight: 600; color: var(--heading-blue); line-height: 16px; }
  .cv-section__title--full { grid-column: 1; margin-bottom: 6px; }
  .cv-label { grid-column: 1; text-align: right; font-size: 9.5px; color: var(--text-grey); line-height: 13px; }
  .cv-text { grid-column: 2; font-size: 7.5px; line-height: 9.5px; color: var(--text-grey); }
  .cv-entry { display: contents; }
  .cv-entry__role { grid-column: 1; text-align: right; font-size: 7px; line-height: 9.6px; color: var(--text-grey); text-transform: uppercase; }
  .cv-entry__sub { grid-column: 1; text-align: right; font-size: 7px; line-height: 9.6px; color: var(--text-grey); }
  .cv-entry__detail { grid-column: 2; font-size: 7px; line-height: 9.6px; color: var(--text-grey); }
  .cv-degree { grid-column: 1; text-align: right; font-size: 9px; line-height: 12px; color: var(--text-grey); }
  .cv-school { grid-column: 2; font-size: 8px; line-height: 11px; color: var(--text-grey); letter-spacing: 0.3px; }

  /* ---------- Cover letter ---------- */
  .letter-page { left: 22px; top: 615px; width: 401px; height: 562px; }
  .letter-title { left: 24px; top: 58px; font-size: 17px; font-weight: 400; color: var(--text-grey); }
  .letter-bands { left: 0; top: 82px; }
  .letter-date { left: 258px; top: 103px; font-size: 7px; color: var(--text-dark); }
  .letter-body { left: 42px; top: 122px; width: 327px; font-size: 7.2px; line-height: 10.2px; color: var(--text-dark); text-align: justify; }
  .letter-body p { margin-bottom: 10px; }
  .letter-body .letter-para--spaced { margin-bottom: 30px; }
  .letter-footer { left: 0; bottom: 0; width: 100%; height: 46px; background: linear-gradient(90deg, #222, #3b3b3b 60%, #454545); }

  /* ---------- Cover page ---------- */
  .cover-page { left: 423px; top: 615px; width: 401px; height: 562px; background: var(--paper); }
  .cover-top { left: 0; top: 0; width: 100%; height: 180px; background: linear-gradient(90deg, #4a4a4a, #5c5c5c 50%, #4c4c4c); }
  .cover-title { left: 53px; top: 112px; font-size: 29px; font-weight: 400; color: var(--paper); }
  .cover-band { left: 0; top: 180px; width: 100%; height: 53px; background: var(--accent-blue); }
  .cover-position { left: 53px; top: 196px; font-size: 14.5px; font-weight: 400; color: var(--paper); }
  .cover-strip { left: 0; top: 233px; width: 100%; height: 13px; background: var(--charcoal-soft); }
  .cover-name { left: 54px; top: 326px; font-size: 13px; color: var(--charcoal); }
  .cover-name__last { color: var(--accent-blue); }
  .cover-contact { left: 54px; top: 352px; font-size: 7px; line-height: 12px; color: var(--text-dark); }
  .cover-accent { left: 0; top: 498px; width: 100%; height: 8px; background: var(--pale-blue); }
  .cover-footer { left: 0; top: 506px; width: 100%; height: 56px; background: linear-gradient(90deg, #222, #353535 60%, #3e3e3e); }
</style>
</head>
<body>

<section class="page cv-page cv-page--one">
  <header class="cv-header">
    <h1 class="cv-name">John <span class="cv-name__last">Doe</span></h1>
    <address class="cv-contact">1234 Street, Town, City, Country, Zip Code<br>Contact Number<br>Email Address</address>
  </header>
  <div class="cv-header__rule"></div>

  <div class="cv-section" style="top:130px">
    <h2 class="cv-section__title">Objective</h2>
    <p class="cv-text" style="grid-row:1 / span 3;padding-top:3px">Lorem ipsum dolor sit amet, consectetur adipiscing elit. Nullam pulvinar volutpat tempor. Lorem ipsum dolor sit amet, consectetur adipiscing elit.</p>
  </div>

  <div class="cv-section" style="top:190px">
    <h2 class="cv-section__title cv-section__title--full">Personal Info</h2>
    <span class="cv-label">Nationality</span>
    <span class="cv-label">Birthday</span>
    <span class="cv-label">Birthplace</span>
  </div>

  <div class="cv-section" style="top:270px">
    <h2 class="cv-section__title cv-section__title--full">Employment</h2>
    <div class="cv-entry"><span class="cv-entry__role">Job Position</span><span class="cv-entry__detail">2000-2009</span></div>
    <div class="cv-entry"><span class="cv-entry__sub">(Employer)</span><span class="cv-entry__detail">(Address)</span></div>
    <div class="cv-entry"><span class="cv-entry__sub"></span><span class="cv-entry__detail">(Description)</span></div>
    <div class="cv-entry"><span class="cv-entry__role">Job Position</span><span class="cv-entry__detail">2000-2009</span></div>
    <div class="cv-entry"><span class="cv-entry__sub">(Employer)</span><span class="cv-entry__detail">(Address)</span></div>
    <div class="cv-entry"><span class="cv-entry__sub"></span><span class="cv-entry__detail">(Description)</span></div>
  </div>

  <div class="cv-section" style="top:364px">
    <h2 class="cv-section__title cv-section__title--full">Education</h2>
    <span class="cv-degree">AB Mass Communications</span><span class="cv-entry__detail" style="line-height:12px">2004-2008</span>
    <span class="cv-degree"></span><span class="cv-school">ELMSTEAD UNIVERSITY</span>
    <span class="cv-degree"></span><span class="cv-entry__detail">Adress</span>
    <span class="cv-degree"></span><span class="cv-entry__detail">(Description)</span>
  </div>

  <footer class="cv-footer"></footer>
</section>

<section class="page cv-page cv-page--two">
  <header class="cv-header">
    <h1 class="cv-name">John <span class="cv-name__last">Doe</span></h1>
    <address class="cv-contact">1234 Street, Town, City, Country, Zip Code<br>Contact Number<br>Email Address</address>
  </header>
  <div class="cv-header__rule"></div>

  <div class="cv-section" style="top:130px">
    <h2 class="cv-section__title">Objective</h2>
    <p class="cv-text" style="grid-row:1 / span 3;padding-top:3px">Lorem ipsum dolor sit amet, consectetur adipiscing elit. Nullam pulvinar volutpat tempor. Lorem ipsum dolor sit amet, consectetur adipiscing elit.</p>
  </div>

  <div class="cv-section" style="top:196px">
    <h2 class="cv-section__title cv-section__title--full">Employment</h2>
    <div class="cv-entry"><span class="cv-entry__role">Job Position</span><span class="cv-entry__detail">2000-2009</span></div>
    <div class="cv-entry"><span class="cv-entry__sub">(Employer)</span><span class="cv-entry__detail">(Address)</span></div>
    <div class="cv-entry"><span class="cv-entry__sub"></span><span class="cv-entry__detail">(Description)</span></div>
    <div class="cv-entry"><span class="cv-entry__role">Job Position</span><span class="cv-entry__detail">2000-2009</span></div>
    <div class="cv-entry"><span class="cv-entry__sub">(Employer)</span><span class="cv-entry__detail">(Address)</span></div>
    <div class="cv-entry"><span class="cv-entry__sub"></span><span class="cv-entry__detail">(Description)</span></div>
  </div>

  <div class="cv-section" style="top:277px">
    <h2 class="cv-section__title cv-section__title--full">Employment</h2>
    <div class="cv-entry"><span class="cv-entry__role">Job Position</span><span class="cv-entry__detail">2000-2009</span></div>
    <div class="cv-entry"><span class="cv-entry__sub">(Employer)</span><span class="cv-entry__detail">(Address)</span></div>
    <div class="cv-entry"><span class="cv-entry__sub"></span><span class="cv-entry__detail">(Description)</span></div>
    <div class="cv-entry"><span class="cv-entry__role">Job Position</span><span class="cv-entry__detail">2000-2009</span></div>
    <div class="cv-entry"><span class="cv-entry__sub">(Employer)</span><span class="cv-entry__detail">(Address)</span></div>
    <div class="cv-entry"><span class="cv-entry__sub"></span><span class="cv-entry__detail">(Description)</span></div>
  </div>

  <div class="cv-section" style="top:357px">
    <h2 class="cv-section__title cv-section__title--full">Employment</h2>
    <div class="cv-entry"><span class="cv-entry__role">Job Position</span><span class="cv-entry__detail">2000-2009</span></div>
    <div class="cv-entry"><span class="cv-entry__sub">(Employer)</span><span class="cv-entry__detail">(Address)</span></div>
    <div class="cv-entry"><span class="cv-entry__sub"></span><span class="cv-entry__detail">(Description)</span></div>
    <div class="cv-entry"><span class="cv-entry__role">Job Position</span><span class="cv-entry__detail">2000-2009</span></div>
    <div class="cv-entry"><span class="cv-entry__sub">(Employer)</span><span class="cv-entry__detail">(Address)</span></div>
    <div class="cv-entry"><span class="cv-entry__sub"></span><span class="cv-entry__detail">(Description)</span></div>
  </div>

  <footer class="cv-footer"></footer>
</section>

<section class="page letter-page">
  <h2 class="abs letter-title">Coverletter</h2>
  <svg class="abs letter-bands" width="401" height="20" viewBox="0 0 401 20" aria-hidden="true">
    <polygon points="0,4 401,0 401,8 0,12" fill="var(--pale-grey)"/>
    <polygon points="0,10 401,6 401,12 0,18" fill="var(--pale-blue)"/>
  </svg>
  <p class="abs letter-date">Date</p>
  <div class="abs letter-body">
    <p>Dear Sir,</p>
    <p class="letter-para--spaced">Lorem ipsum dolor sit amet, consectetur adipiscing elit. Quisque dictum leo quis mauris dictum auctor. Praesent viverra, elit at rutrum fringilla, purus nisl feugiat est, sit amet lobortis magna mauris id nibh. Sed interdum massa non mauris faucibus cursus. Integer at tellus sit amet lacus ultrices ullamcorper. Nunc vel libero dui, sit amet pellentesque ligula. Suspendisse semper, urna.</p>
    <p class="letter-para--spaced">Aenean quis nisi arcu, blandit mollis odio. Vestibulum nulla enim, viverra a auctor quis, suscipit rhoncus libero. Donec quis libero vel magna luctus pulvinar. Duis eget nulla vel massa commodo semper placerat id leo. Nunc eu leo quis lorem hendrerit accumsan. Maecenas eleifend nisi non velit dignissim ut suscipit arcu imperdiet. Phasellus nisi nulla, tincidunt. Proin tincidunt, est sed rhoncus mattis, nunc sem aliquet quam, eget tristique augue dolor vel orci. Vestibulum et tellus dui, vitae sollicitudin sapien. Pellentesque nisl tortor, faucibus in mollis non, dignissim et felis.</p>
    <p>Phasellus nisi nulla, tincidunt. Proin tincidunt, est sed rhoncus mattis, nunc sem aliquet quam, eget tristique augue dolor vel orci. Vestibulum et tellus dui, vitae sollicitudin sapien. Pellentesque nisl tortor, faucibus in mollis non, dignissim et felis.</p>
    <p style="margin-bottom:8px">Sincerely,</p>
    <p>Good Looking</p>
  </div>
  <div class="abs letter-footer"></div>
</section>

<section class="page cover-page">
  <div class="abs cover-top"></div>
  <h1 class="abs cover-title">Application</h1>
  <div class="abs cover-band"></div>
  <p class="abs cover-position">Job Position Here</p>
  <div class="abs cover-strip"></div>
  <p class="abs cover-name">John <span class="cover-name__last">Doe</span></p>
  <address class="abs cover-contact">48 Corwen Lane, Apt.# XXX<br>Haldenport, QA 40712<br>Country<br>Mobil : +0 (100) 234 5678<br>E-Mail : someone@mailbox.test</address>
  <div class="abs cover-accent"></div>
  <div class="abs cover-footer"></div>
</section>

</body>
</html>
```